Criminal Defense Firm looking for an edge in business card design

Established Criminal Defense Firm looking to refresh business card. We already have logo and website, but our business cards are extremely boring. We would like to also have something on the backside of card.
Needs to be business oriented, but creative.
We provide services to professionals such as doctors, lawyers, politicians, etc.
Our specialty is to protect professional licenses when facing a criminal matter.

Update on March 10, 2015: This project is for a Business Card Design. The winner in this project will be assigned the next (1on1) project which incidentally is also entitled Business Card Design. I'm sorry for this confusion. The 1on1 project will not be for Business Card Design but will be for Stationery-Envelope Design. Thank you for your attention and continued participation.

Target Market(s)

People accused of a crime

Industry/Entity Type

Business

Contact Information for Business Card

Simple, strong, professional

Colors
85abd2
3176b5
0355a3

```html
<!DOCTYPE html>
<html lang="en">
<head>
<meta charset="utf-8">
<title>Whitcombe Ashford Law Corporation — Business Cards</title>
<link href="https://fonts.googleapis.com/css2?family=Cinzel:wght@500;700&family=Crimson+Text:ital,wght@0,400;1,400&family=Open+Sans:wght@400&display=swap" rel="stylesheet">
<style>
  :root {
    --backdrop: #e9e9ec;
    --paper: #ffffff;
    --brand-blue: #1f57a2;
    --brand-mid: #3176b5;
    --ink: #1a1a1a;
    --ink-soft: #3a3a3a;
  }
  * { box-sizing: border-box; margin: 0; padding: 0; }
  html, body { width: 1200px; height: 768px; overflow: hidden; }
  body { background: var(--backdrop); position: relative; }

  .card {
    position: absolute;
    width: 520px;
    height: 298px;
    background: var(--paper);
    box-shadow: 0 6px 18px rgba(0,0,0,.18);
    overflow: hidden;
  }
  .card--back { left: 50px; top: 235px; }
  .card--front { left: 630px; top: 235px; }

  /* Back card */
  .brand-lockup {
    position: absolute; left: 86px; top: 26px;
    display: flex; align-items: center; gap: 14px;
  }
  .brand-mark {
    width: 58px; height: 58px; border-radius: 50%;
    border: 3px solid var(--brand-blue);
    flex: none;
  }
  .brand-name {
    font-family: "Cinzel", serif; font-weight: 700;
    color: var(--brand-blue); font-size: 21px; line-height: .95;
    letter-spacing: .5px;
  }
  .brand-sub {
    font-family: "Crimson Text", serif; font-style: italic;
    color: var(--brand-blue); font-size: 14px;
    margin-left: 110px; margin-top: 2px; display: block;
  }
  .tagline {
    position: absolute; left: 0; right: 0; top: 112px;
    text-align: center;
    font-family: "Crimson Text", serif; text-transform: uppercase;
    font-size: 14px; line-height: 1.32; color: var(--ink-soft);
    letter-spacing: .3px;
  }
  .back-band {
    position: absolute; left: 0; right: 0; top: 224px; height: 46px;
    background: var(--brand-blue);
    display: flex; align-items: center; justify-content: center;
  }
  .web {
    font-family: "Open Sans", sans-serif; color: #ffffff; font-size: 15px;
  }

  /* Front card */
  .front-mark {
    position: absolute; left: 44px; top: 46px;
    width: 150px; height: 150px; border-radius: 50%;
    border: 5px solid var(--brand-blue);
  }
  .front-band {
    position: absolute; left: 0; right: 0; bottom: 0; height: 16px;
    background: var(--brand-blue);
  }
  .firm {
    position: absolute; right: 30px; top: 40px; text-align: right;
  }
  .firm-name {
    font-family: "Cinzel", serif; font-weight: 700; color: var(--ink);
    font-size: 21px; line-height: .95; letter-spacing: .5px;
  }
  .firm-sub {
    font-family: "Crimson Text", serif; font-style: italic;
    color: var(--ink); font-size: 14px; display: block; margin-top: 1px;
  }
  .person {
    position: absolute; right: 30px; top: 118px; text-align: right;
  }
  .person-name {
    font-family: "Cinzel", serif; font-weight: 700; color: var(--brand-blue);
    font-size: 18px; letter-spacing: .6px;
  }
  .person-role {
    font-family: "Crimson Text", serif; font-style: italic;
    font-size: 15px; color: var(--ink-soft);
  }
  .contact {
    position: absolute; right: 30px; top: 176px; text-align: right;
    font-family: "Open Sans", sans-serif; font-size: 13px; line-height: 1.45;
    color: var(--ink-soft); list-style: none;
  }
  .contact li { display: flex; justify-content: flex-end; align-items: center; gap: 8px; }
  .contact .icon { width: 13px; height: 13px; fill: var(--brand-blue); flex: none; }
  .contact .no-icon { padding-right: 21px; }
</style>
</head>
<body>

  <section class="card card--back" aria-label="Card back">
    <div class="brand-lockup">
      <span class="brand-mark" aria-hidden="true"></span>
      <div>
        <div class="brand-name">Whitcombe<br>Ashford</div>
        <span class="brand-sub">Law Corporation</span>
      </div>
    </div>
    <p class="tagline">
      We provide services to professionals<br>
      such as doctors, lawyers, politicians, etc.<br>
      Our specialty is to protect professional<br>
      licenses when facing a criminal matter
    </p>
    <div class="back-band"><span class="web">www.wacriminaldefense.com</span></div>
  </section>

  <section class="card card--front" aria-label="Card front">
    <span class="front-mark" aria-hidden="true"></span>
    <div class="firm">
      <div class="firm-name">Whitcombe<br>Ashford</div>
      <span class="firm-sub">Law Corporation</span>
    </div>
    <div class="person">
      <div class="person-name">Daniel Whitcombe</div>
      <div class="person-role">Attorney at Law</div>
    </div>
    <ul class="contact">
      <li>555-210-4470
        <svg class="icon" viewBox="0 0 16 16" aria-hidden="true"><path d="M2 5c0-2 2-3 6-3s6 1 6 3v1h-3V4.5H5V6H2zM4 7h8l2 6H2z"/></svg></li>
      <li>555-210-4471
        <svg class="icon" viewBox="0 0 16 16" aria-hidden="true"><path d="M2 5c0-2 2-3 6-3s6 1 6 3v1h-3V4.5H5V6H2zM4 7h8l2 6H2z"/></svg></li>
      <li>daniel@wacriminaldefense.com
        <svg class="icon" viewBox="0 0 16 16" aria-hidden="true"><path d="M1 3h14v10H1zM2 4l6 5 6-5z" fill-rule="evenodd"/></svg></li>
      <li class="no-icon">1180 Alder Avenue, Suite 210</li>
      <li class="no-icon">Riverton, California 90000</li>
    </ul>
    <div class="front-band"></div>
  </section>

</body>
</html>
```